Need five new images

Design five images for our website.
================================
Please follow the details in this document:
https://files.plumbrook.example/open?id=7Q42TrWnUzd9Hb1mxRqPaXcnoe5
Additional details
Draw attention to free diagnosis
-
Draw attention to the call to action ( phone call )
-
The steps 1, 2, 3 images should use some kind of logical progression indicator and the information about each step whould be contained in a web box. Link to example of progression indicators and web boxes that we like:

http://vexomart.example/item/pricing-plans-buttons-steps-special-offer/47213?WT.ac=search_thumb&WT.seg_1=search_thumb&WT.z_author=truvelin)

Target Market(s)

Business owners and home computer users that need tech support.

Industry/Entity Type

Call

Requirements
Must have
• The design is 5 images: 900x300 for STEP123-HOMEPAGE, 900x345 STEP123-CART, 536x345 for slider_img_01, 536x345 for slider_img_02, 536x345 for slider_img_03.
Nice to have
• It would be nice see 2 design options for the sliders (one using vector images of people, and another using photos of real people).
Should not have
• no handwritten fonts, no cartoon super heroes (Gochi Hand font is used in logo only)

```html
<!DOCTYPE html>
<html lang="en">
<head>
<meta charset="utf-8">
<title>Three Steps to Repair</title>
<link href="https://fonts.googleapis.com/css2?family=Source+Sans+3:wght@400;600;700&display=swap" rel="stylesheet">
<style>
  :root {
    --blue: #4a8fd6;
    --grey: #9a9a9a;
    --green: #4f9a4c;
    --text-grey: #8c8c8c;
    --divider: #b5b5b5;
    --white: #ffffff;
    --badge-gold: #f2b51c;
    --badge-dark: #3a3a3a;
    --badge-teal: #3fa9a0;
  }
  * { margin: 0; padding: 0; box-sizing: border-box; }
  html, body {
    width: 1200px; height: 460px; overflow: hidden;
    background: var(--white);
    font-family: "Source Sans 3", "Helvetica Neue", Arial, sans-serif;
  }
  .steps { position: relative; width: 1200px; height: 460px; }
  .step {
    position: absolute; top: 40px; width: 300px;
    display: flex; flex-direction: column; align-items: center; text-align: center;
  }
  .step--call { left: 57px; }
  .step--diagnosis { left: 450px; }
  .step--guarantee { left: 882px; }
  .step__label {
    width: 262px; height: 87px; border-radius: 6px;
    color: var(--white); font-weight: 700; font-size: 62px; letter-spacing: 1px;
    display: flex; align-items: center; justify-content: center; line-height: 1;
  }
  .step--call .step__label { background: var(--blue); }
  .step--diagnosis .step__label { background: var(--grey); }
  .step--guarantee .step__label { background: var(--green); }
  .divider {
    position: absolute; top: 129px; width: 2px; height: 264px; background: var(--divider);
  }
  .divider--first { left: 408px; }
  .divider--second { left: 824px; }

  .call__intro { margin-top: 34px; color: var(--blue); font-size: 25px; font-weight: 600; line-height: 1; }
  .call__phone { margin-top: 8px; color: var(--blue); font-size: 44px; font-weight: 600; line-height: 1; letter-spacing: 0.5px; }
  .call__note { margin-top: 10px; color: var(--blue); font-size: 20px; font-weight: 600; line-height: 1; }
  .call__badges { margin-top: 14px; display: flex; gap: 40px; align-items: center; }

  .diagnosis__lead { margin-top: 120px; color: var(--text-grey); font-size: 27px; font-weight: 600; line-height: 1; }
  .diagnosis__free { margin-top: 10px; color: var(--green); font-size: 48px; font-weight: 700; line-height: 1; }
  .diagnosis__tail { margin-top: 12px; color: var(--text-grey); font-size: 25px; font-weight: 600; line-height: 1; }

  .guarantee__lead { margin-top: 34px; color: var(--green); font-size: 25px; font-weight: 700; line-height: 28px; }
  .guarantee__highlight { color: var(--blue); font-weight: 700; line-height: 44px; }
  .guarantee__percent { font-size: 40px; }
  .guarantee__words { font-size: 42px; letter-spacing: 0.5px; }
</style>
</head>
<body>
<main class="steps">
  <section class="step step--call">
    <div class="step__label">STEP 1</div>
    <p class="call__intro">CALL US FOR FREE ON</p>
    <p class="call__phone">1-888-555-0142</p>
    <p class="call__note">answered in less than a minute</p>
    <div class="call__badges">
      <svg class="badge badge--security" width="100" height="56" viewBox="0 0 100 56" role="img" aria-label="Security badge">
        <circle cx="22" cy="24" r="18" fill="var(--badge-gold)"/>
        <rect x="44" y="14" width="52" height="22" rx="4" fill="var(--badge-dark)"/>
        <rect x="10" y="46" width="80" height="5" rx="2" fill="#c9c9c9"/>
      </svg>
      <svg class="badge badge--partner" width="100" height="56" viewBox="0 0 100 56" role="img" aria-label="Partner badge">
        <rect x="74" y="2" width="20" height="20" rx="3" fill="var(--badge-teal)"/>
        <rect x="4" y="30" width="92" height="12" rx="3" fill="var(--badge-dark)"/>
      </svg>
    </div>
  </section>

  <div class="divider divider--first"></div>

  <section class="step step--diagnosis">
    <div class="step__label">STEP 2</div>
    <p class="diagnosis__lead">WE GIVE YOU A</p>
    <p class="diagnosis__free">FREE</p>
    <p class="diagnosis__tail">DIAGNOSIS</p>
  </section>

  <div class="divider divider--second"></div>

  <section class="step step--guarantee">
    <div class="step__label">STEP 3</div>
    <p class="guarantee__lead">Get a fixed price<br>for repair with no<br>hidden extras and a</p>
    <p class="guarantee__highlight">
      <span class="guarantee__percent">100%</span><br>
      <span class="guarantee__words">MONEY BACK<br>GUARANTEE</span>
    </p>
  </section>
</main>
</body>
</html>
```